Varnath Consulting Business card design.

See our website www.varnathconsulting-example.com which will give you a good idea of what we are about. The font is called 'Play'.

I'd like a standout business card in keeping with the themes and branding on the website

Target Market(s)

professionals. HR directors

Industry/Entity Type

Business

Contact Information for Business Card

Varnath Consulting PO Box 3917 Tindale Creek NSW 2840 1300 457 318 Gerald Ashbury Principal email: jobs@varnathconsulting-example.com ABN: 31792048663

Font styles to use
Other font styles liked:
• Play

Requirements
Must have
• Must have same design colours and branding as website.
• On back I'd prefer a list of the things we do which appears below the name at the header on the website

```html
<!DOCTYPE html>
<html lang="en">
<head>
<meta charset="utf-8">
<title>Varnath Consulting – Business Card</title>
<link rel="stylesheet" href="https://fonts.googleapis.com/css2?family=Open+Sans:wght@400;600;700&display=swap">
<style>
  :root {
    --brand-red: #b31217;
    --brand-grey: #56565a;
    --card-white: #ffffff;
    --stage: #ececec;
    --text-light: #ffffff;
  }
  * { margin: 0; padding: 0; box-sizing: border-box; }
  html, body {
    width: 1200px; height: 900px; overflow: hidden;
    background: var(--stage);
    font-family: "Open Sans", Arial, sans-serif;
  }
  .canvas { position: relative; width: 1200px; height: 900px; }

  .card {
    position: absolute;
    background: var(--card-white);
    box-shadow: 0 6px 18px rgba(0,0,0,0.15);
    overflow: hidden;
  }

  /* Front */
  .card--front { left: 77px; top: 35px; width: 588px; height: 362px; }
  .front__header {
    position: absolute; left: 0; top: 0; width: 100%; height: 155px;
    display: flex; align-items: center; padding-left: 34px; gap: 26px;
  }
  .brand-dot {
    width: 56px; height: 56px; border-radius: 50%;
    background: var(--brand-red); flex: none;
  }
  .brand-name {
    color: var(--brand-red); font-weight: 400; line-height: 1;
    display: flex; flex-direction: column; gap: 8px;
  }
  .brand-name__main { font-size: 46px; letter-spacing: 1px; }
  .brand-name__sub { font-size: 27px; letter-spacing: 4px; }

  .front__body {
    position: absolute; left: 0; top: 155px; width: 100%; height: 207px;
    background: var(--brand-red); color: var(--text-light);
    padding: 22px 0 0 33px;
  }
  .person__name { font-size: 19px; font-weight: 700; line-height: 1.1; }
  .person__role { font-size: 15px; margin-top: 2px; }
  .details { list-style: none; margin-top: 17px; font-size: 15px; }
  .details li { display: flex; align-items: center; gap: 9px; height: 25px; }
  .details li.abn { margin-bottom: 6px; }
  .details li.postal { margin-top: 3px; }
  .details b { font-weight: 700; }
  .icon { width: 12px; height: 12px; fill: var(--text-light); flex: none; }

  /* Back */
  .card--back { left: 388px; top: 505px; width: 567px; height: 352px; }
  .back__band {
    position: absolute; left: 0; top: 110px; width: 100%; height: 130px;
    background: var(--brand-red);
    display: flex; align-items: center; justify-content: center;
  }
  .back__band .brand-name { color: var(--text-light); align-items: center; }
  .back__band .brand-name__main { font-size: 52px; }
  .back__band .brand-name__sub { font-size: 28px; letter-spacing: 5px; }
</style>
</head>
<body>
<main class="canvas">

  <section class="card card--front" aria-label="Business card front">
    <header class="front__header">
      <span class="brand-dot" aria-hidden="true"></span>
      <div class="brand-name">
        <span class="brand-name__main">VARNATH</span>
        <span class="brand-name__sub">CONSULTING</span>
      </div>
    </header>
    <div class="front__body">
      <p class="person__name">Gerald Ashbury</p>
      <p class="person__role">Principal</p>
      <ul class="details">
        <li class="abn"><span><b>ABN:</b> 31792048663</span></li>
        <li>
          <svg class="icon" viewBox="0 0 24 24" aria-hidden="true"><path d="M6.6 10.8a15.1 15.1 0 0 0 6.6 6.6l2.2-2.2a1 1 0 0 1 1-.25 11.4 11.4 0 0 0 3.6.57 1 1 0 0 1 1 1V20a1 1 0 0 1-1 1A17 17 0 0 1 3 4a1 1 0 0 1 1-1h3.5a1 1 0 0 1 1 1c0 1.25.2 2.45.57 3.57a1 1 0 0 1-.25 1z"/></svg>
          <span>1300 457 318</span>
        </li>
        <li>
          <svg class="icon" viewBox="0 0 24 24" aria-hidden="true"><path d="M2 5h20v14H2z M2 5l10 8 10-8" fill="var(--text-light)"/><path d="M3 6l9 7 9-7" fill="none" stroke="var(--brand-red)" stroke-width="2"/></svg>
          <span>jobs@varnathconsulting-example.com</span>
        </li>
        <li class="postal"><span>PO Box 3917 Tindale Creek NSW 2840</span></li>
      </ul>
    </div>
  </section>

  <section class="card card--back" aria-label="Business card back">
    <div class="back__band">
      <div class="brand-name">
        <span class="brand-name__main">VARNATH</span>
        <span class="brand-name__sub">CONSULTING</span>
      </div>
    </div>
  </section>

</main>
</body>
</html>
```